New Business Cards for Torvin Group

We need a new Business Card to compliment our new logo. We are a vibrant design, manufacture and install business providing recreation areas, public parks and Municipal spaces. We want business cards that are classy, modern and clean.

We have recently changed our logo, and are celebrating our 40th anniversary. We want business cards with a new modern design to reflect our status.

Target Market(s)

Customers

Contact Information for Business Card

We need all the details of our 3 offices as per the business card attached. Please disregard the old logo on the business card, the other three files show our new logo.

Requirements
Must have
• All info as per attached business card but with new logo.
Nice to have

```html
<!DOCTYPE html>
<html lang="en">
<head>
<meta charset="utf-8">
<title>Torvin Group Business Card</title>
<link href="https://fonts.googleapis.com/css2?family=Lato:wght@400;700&display=swap" rel="stylesheet">
<style>
  :root {
    --stage: #5c5c5e;
    --paper: #ffffff;
    --charcoal: #4a4a4d;
    --ink: #2f2f31;
    --muted: #66666a;
    --red: #e8333a;
    --rule: #55555a;
  }
  * { margin: 0; padding: 0; box-sizing: border-box; }
  html, body { width: 1200px; height: 1200px; overflow: hidden; }
  body {
    background: var(--stage);
    font-family: "Lato", sans-serif;
    position: relative;
  }
  .card {
    position: absolute;
    left: 240px;
    width: 720px;
    height: 420px;
    border-radius: 36px;
    overflow: hidden;
  }
  .card-front { top: 142px; background: var(--paper); }
  .card-back { top: 638px; background: var(--charcoal); }

  .name-tab {
    position: absolute; left: 0; top: 90px;
    width: 10px; height: 50px;
    background: var(--red); border-radius: 0 4px 4px 0;
  }
  .holder-name {
    position: absolute; left: 24px; top: 84px;
    font-size: 26px; font-weight: 700; color: var(--red);
  }
  .holder-title {
    position: absolute; left: 24px; top: 120px;
    font-size: 17px; color: var(--ink);
  }
  .direct-contact {
    position: absolute; left: 24px; top: 181px;
    font-size: 13.5px; color: var(--ink); line-height: 28px;
    list-style: none;
  }
  .direct-contact .label { color: var(--red); }
  .divider {
    position: absolute; left: 24px; top: 245px;
    width: 662px; height: 1.5px; background: var(--rule);
  }
  .office {
    position: absolute; top: 258px;
    list-style: none; font-size: 13.3px; color: var(--muted); line-height: 21.6px;
  }
  .office h2 {
    font-size: 17.5px; font-weight: 400; color: var(--red);
    line-height: 26px; margin-bottom: 3px;
  }
  .office-head { left: 24px; }
  .office-dubai { left: 275px; }
  .office-qatar { left: 505px; top: 260px; }

  .footer-band { position: absolute; left: 0; bottom: 0; width: 720px; height: 38px; }
  .footer-web {
    position: absolute; left: 24px; bottom: 12px;
    font-size: 13.5px; color: #fff;
  }

  .wordmark {
    position: absolute; display: flex; align-items: center; gap: 12px;
    font-weight: 700; white-space: nowrap;
  }
  .wordmark .dot { border-radius: 50%; background: var(--red); flex: none; }
  .wordmark-front { right: 34px; top: 70px; font-size: 30px; color: var(--charcoal); }
  .wordmark-front .dot { width: 40px; height: 40px; }
  .wordmark-back {
    left: 50%; top: 210px; transform: translate(-50%, -50%);
    font-size: 44px; color: #fff; gap: 16px;
  }
  .wordmark-back .dot { width: 56px; height: 56px; }
  .back-web {
    position: absolute; left: 0; right: 0; top: 374px;
    text-align: center; font-size: 14px; font-weight: 700; color: #fff;
  }
  .back-web span { color: var(--red); }
</style>
</head>
<body>
  <section class="card card-front">
    <div class="name-tab"></div>
    <h1 class="holder-name">Marek Dalloway</h1>
    <p class="holder-title">Managing Partner</p>
    <div class="wordmark wordmark-front"><span class="dot"></span>Torvin Group</div>
    <ul class="direct-contact">
      <li><span class="label">Phone:</span> +971 (0)50 318 4702</li>
      <li><span class="label">Email:</span> marek@torvingroup.com</li>
    </ul>
    <div class="divider"></div>
    <ul class="office office-head">
      <li><h2>Head Office</h2></li>
      <li>P.O. Box: 41820 Abu Dhabi. U.A.E</li>
      <li>Tel No: +971 (0)2 5827310</li>
      <li>Fax No: +971(0)2 5827311</li>
      <li>Email: sales@torvingroup.com</li>
    </ul>
    <ul class="office office-dubai">
      <li><h2>Dubai Office</h2></li>
      <li>P.O. Box: 270416 Dubai, U.A.E</li>
      <li>Tel No: +971 (0)4 683205</li>
      <li>Fax No: +971(0)4 683297</li>
      <li>Email: sales@torvingroup.com</li>
    </ul>
    <ul class="office office-qatar">
      <li><h2>Qater Office</h2></li>
      <li>P.O. Box: 30972 Doha, Qatter</li>
      <li>Tel No: +974 44715386</li>
      <li>Fax No: +971 44520973</li>
      <li>Email: sales@torvingroup.com</li>
    </ul>
    <svg class="footer-band" viewBox="0 0 720 38" aria-hidden="true">
      <rect x="0" y="18" width="720" height="20" fill="var(--charcoal)"/>
      <path d="M0 0 H222 Q232 0 238 8 L260 38 H0 Z" fill="#ffffff"/>
      <path d="M0 0 H216 Q226 0 232 8 L254 38 H0 Z" fill="var(--red)"/>
    </svg>
    <p class="footer-web">www.torvingroup.com</p>
  </section>

  <section class="card card-back">
    <div class="wordmark wordmark-back"><span class="dot"></span>Torvin Group</div>
    <p class="back-web">www.<span>torvingroup</span>.com</p>
  </section>
</body>
</html>
```